Fahrzeugbeschriftung für einen Hofladen
Zielgruppe
Biologische Produkte an den Endverbraucher vermarkten. Vorallem Kartoffel, Eier und Getreide.
24 h Hofladen
Aufgabenstellung
ansprechendes Design mit unseren Logo
Es soll das vorhandene Logo + Telfonnummer,Ort und Homepage oben stehn.
KL Lastwiesel R8 Kastenwagen (In Fahrtrichtung links Befindet sich auf der Seite ein Lufthutze)

```html
<!DOCTYPE html>
<html lang="de">
<head>
<meta charset="utf-8">
<title>Grünhof Lindner – Fahrzeugbeschriftung</title>
<link rel="stylesheet" href="https://fonts.googleapis.com/css2?family=Ubuntu:wght@400;500;700&display=swap">
<style>
  :root {
    --farm-green: #b7c244;
    --earth-brown: #6f6663;
    --text-grey: #5e5a58;
    --panel-white: #ffffff;
    --page-bg: #f3f3f1;
  }
  html, body {
    margin: 0;
    padding: 0;
    overflow: hidden;
    background: var(--page-bg);
  }
  .vehicle-livery {
    position: relative;
    width: 1200px;
    height: 728px;
    overflow: hidden;
    background: var(--panel-white);
    font-family: "Ubuntu", sans-serif;
  }

  .brand-name {
    position: absolute;
    left: 110px;
    top: 110px;
    display: flex;
    align-items: center;
    gap: 26px;
  }
  .brand-dot {
    width: 60px;
    height: 60px;
    border-radius: 50%;
    background: var(--farm-green);
  }
  .brand-text {
    margin: 0;
    font-size: 72px;
    font-weight: 400;
    line-height: 1.05;
    color: var(--text-grey);
  }

  .contact-block {
    position: absolute;
    left: 760px;
    top: 118px;
  }
  .contact-phone {
    margin: 0 0 14px;
    font-size: 40px;
    font-weight: 700;
    color: var(--farm-green);
    letter-spacing: 0.5px;
  }
  .contact-address {
    margin: 0 0 0 52px;
    font-style: normal;
    font-size: 22px;
    line-height: 1.35;
    color: var(--text-grey);
  }

  .base-rule {
    position: absolute;
    left: 0;
    right: 0;
    top: 540px;
    height: 10px;
    background: var(--earth-brown);
  }
  .base-band {
    position: absolute;
    left: 0;
    right: 0;
    top: 570px;
    bottom: 0;
    background: var(--farm-green);
  }
  .website {
    position: absolute;
    left: 0;
    right: 0;
    top: 620px;
    margin: 0;
    text-align: center;
    font-size: 38px;
    font-weight: 400;
    color: var(--earth-brown);
  }
</style>
</head>
<body>
  <main class="vehicle-livery">
    <header class="brand-name">
      <span class="brand-dot"></span>
      <h1 class="brand-text">Grünhof<br>Lindner</h1>
    </header>

    <section class="contact-block">
      <p class="contact-phone">02284/51967</p>
      <address class="contact-address">
        Grünhof Lindner<br>
        Wiesenweg 7<br>
        3452 Kornfeld
      </address>
    </section>

    <div class="base-rule"></div>
    <div class="base-band"></div>
    <p class="website">www.gruenhof-lindner.at</p>
  </main>
</body>
</html>
```